Harriet Voss Consortium - Paediatric Lower Limb Surgery Agenda Forming Collective

A 2-sided A4 leaflet to explain the research priorities in Children's Orthopaedic Surgery.
We would like this to be similar to that produced previously by the physiotherapists.

```html
<!DOCTYPE html>
<html lang="en">
<head>
<meta charset="utf-8">
<title>Harriet Voss Consortium – Research Priorities Leaflet</title>
<link href="https://fonts.googleapis.com/css2?family=Didact+Gothic&family=Fredoka:wght@500;600&family=Open+Sans:wght@400;600;700&display=swap" rel="stylesheet">
<style>
  :root{
    --bg:#8a8a8a;
    --blue-deep:#134f9e;
    --blue:#1d6cc4;
    --blue-light:#3a9be6;
    --yellow:#f8c500;
    --purple:#4a2a86;
    --magenta:#b51e8c;
    --green:#137a3a;
    --orange:#f08a1c;
    --red:#d4202f;
    --teal:#11a39a;
    --white:#ffffff;
    --ink:#1d2b55;
    --maroon:#9b1b2a;
  }
  *{box-sizing:border-box;margin:0;padding:0}
  html,body{width:960px;height:1200px;overflow:hidden}
  body{background:radial-gradient(circle at 50% 50%,#a9a9a9,var(--bg));font-family:"Open Sans",sans-serif;position:relative}
  .page{position:absolute;top:282px;width:450px;height:636px;overflow:hidden;box-shadow:0 4px 18px rgba(0,0,0,.35)}
  .page--front{left:20px;background:linear-gradient(180deg,var(--blue-deep) 0%,var(--blue) 35%,var(--blue-light) 55%,#cfe4f7 68%,#fff 76%)}
  .page--back{left:490px;background:linear-gradient(180deg,var(--blue-deep) 0%,var(--blue) 40%,var(--blue-light) 85%)}
  .abs{position:absolute}

  /* Front */
  .brand-box{left:26px;top:14px;width:156px;height:82px;background:var(--white);padding:8px 10px;display:flex;flex-direction:column;justify-content:space-between}
  .brand-name{display:flex;align-items:center;gap:7px;font-family:"Didact Gothic",sans-serif;color:var(--maroon);font-size:19px;line-height:1}
  .brand-mark{width:22px;height:22px;background:var(--maroon);flex:none}
  .brand-tag{font-size:8.5px;color:#333}
  .site-url{right:26px;top:16px;color:var(--white);font-size:10px;font-weight:600}
  .title{left:26px;top:104px;width:400px;font-family:"Fredoka",sans-serif;color:var(--yellow)}
  .title h1{font-size:26px;font-weight:600;letter-spacing:.5px}
  .title p{font-size:19px;font-weight:500;line-height:1.4}
  .intro{left:26px;top:212px;width:400px;color:var(--white);font-size:10.2px;line-height:1.3}
  .intro p+p{margin-top:10px}

  .stage-box{border-radius:10px;color:var(--white);padding:8px 12px}
  .stage-box h2{font-size:12.5px;font-weight:700}
  .stage-box p{font-size:8.6px;line-height:1.3}
  .stage-box--ask{left:105px;top:352px;width:316px;height:78px;background:var(--purple);padding-left:18px}
  .stage-box--analyse{left:40px;top:446px;width:330px;height:76px;background:var(--green);padding-top:14px}
  .stage-box--prior{left:105px;top:538px;width:316px;height:76px;background:var(--red);padding-left:18px}
  .stage-box h2+p{margin-top:2px}
  .stage-dot{width:76px;height:76px;border-radius:50%;border:4px solid var(--white);color:var(--white);text-align:center;font-family:"Fredoka",sans-serif;box-shadow:0 2px 6px rgba(0,0,0,.3)}
  .stage-dot span{display:block;font-size:11px;font-weight:600;margin-top:8px}
  .stage-dot b{display:block;font-size:38px;font-weight:600;line-height:.95}
  .stage-dot--1{left:36px;top:352px;background:radial-gradient(circle at 40% 35%,#e04bb0,var(--magenta))}
  .stage-dot--2{left:350px;top:446px;background:radial-gradient(circle at 40% 35%,#ffe04a,var(--orange))}
  .stage-dot--3{left:36px;top:538px;background:radial-gradient(circle at 40% 35%,#4aa8ff,#1268d1)}
  .front-foot{left:0;bottom:0;width:100%;height:5px;background:var(--purple)}

  /* Back */
  .heading-banner{left:62px;top:8px;width:326px;height:38px}
  .heading-banner h2{position:absolute;inset:0;text-align:center;line-height:38px;color:var(--white);font-family:"Didact Gothic",sans-serif;font-size:18px}
  .priority{left:22px;width:406px;height:40px;background:rgba(255,255,255,.93);border-radius:20px;display:flex;align-items:center;color:var(--ink);font-size:8.6px;line-height:1.3;text-align:justify}
  .priority--l{padding:0 14px 0 38px}
  .priority--r{padding:0 38px 0 24px}
  .num{width:44px;height:44px;clip-path:polygon(30% 0,70% 0,100% 30%,100% 70%,70% 100%,30% 100%,0 70%,0 30%);color:var(--white);font-family:"Fredoka",sans-serif;font-size:22px;font-weight:600;display:flex;align-items:center;justify-content:center}
  .num--l{left:6px}
  .num--r{right:6px}
  .c-red{background:var(--red)}.c-green{background:var(--green)}.c-orange{background:var(--orange)}.c-purple{background:var(--purple)}.c-teal{background:var(--teal)}
  .thanks-band{left:0;top:542px;width:100%;height:20px;background:var(--red);color:var(--white);font-size:8.5px;text-align:center;line-height:20px}
  .sponsors{left:0;top:562px;width:100%;height:70px;background:var(--white)}
  .sponsors__label{left:10px;top:24px;font-size:9.5px;color:var(--ink);line-height:1.25}
  .sponsor{display:flex;align-items:center;gap:5px;font-size:10px;font-weight:700}
  .sponsor i{width:10px;height:10px;flex:none}
  .sponsor--guild{left:66px;top:30px;color:var(--maroon)}
  .sponsor--guild i{background:var(--maroon)}
  .sponsor--society{left:172px;top:12px;color:var(--red)}
  .sponsor--society i{background:var(--red)}
  .sponsor--uni{left:172px;top:44px;color:#1b2a5a}
  .sponsor--uni i{border-radius:50%;background:#1b2a5a}
  .sponsor-end{right:12px;top:6px;text-align:right;font-size:7.5px;color:var(--ink);line-height:1.3}
  .sponsor-end .brand-name{font-size:14px;justify-content:flex-end;margin:2px 0}
  .sponsor-end .brand-mark{width:14px;height:14px}
  .back-foot{left:0;bottom:0;width:100%;height:4px;background:var(--yellow)}
</style>
</head>
<body>

<section class="page page--front" aria-label="Leaflet front">
  <svg class="abs" width="450" height="636" viewBox="0 0 450 636" aria-hidden="true" style="left:0;top:0">
    <path d="M0 200 Q220 120 450 180" stroke="rgba(255,255,255,.35)" fill="none" stroke-width="1.2"/>
    <path d="M300 40 L420 0" stroke="rgba(255,255,255,.35)" fill="none" stroke-width="1.2"/>
    <path d="M200 280 Q260 210 340 250 L380 320 Q300 360 200 320 Z" fill="rgba(255,255,255,.07)"/>
  </svg>
  <div class="abs brand-box">
    <div class="brand-name"><span class="brand-mark"></span>Harriet Voss Consortium</div>
    <div class="brand-tag">Agenda Forming Collectives</div>
  </div>
  <div class="abs site-url">www.hvc-research.org.uk</div>
  <div class="abs title">
    <h1>Harriet Voss Consortium -</h1>
    <p>Paediatric Lower Limb Surgery<br>Agenda Forming Collective</p>
  </div>
  <div class="abs intro">
    <p>Surgery is often carried out amongst children with conditions that their legs, but in many conditions, it is not known which treatment works best. We need high-quality research to test which treatments are better for children.</p>
    <p>We reached out to everybody involved with children who have orthopaedic problems affecting their legs (from hip to toes), including children, parents, carers, charity workers, and all the professional groups. We asked all for their views on identifying the most important unanswered questions.</p>
  </div>

  <div class="abs stage-box stage-box--ask">
    <h2>ASK</h2>
    <p>Our UK-wide survey of patients, carers, physiotherapists, nurses and surgeons asked</p>
    <p>“What is the most important unanswered question amongst children undergoing planned surgery for conditions affecting their legs”</p>
  </div>
  <div class="abs stage-dot stage-dot--1"><span>STAGE</span><b>1</b></div>

  <div class="abs stage-box stage-box--analyse">
    <h2>ANALYSE</h2>
    <p>We reviewed 1023 questions from 388 people, and sorted these into<br>76 unique themed questions.</p>
  </div>
  <div class="abs stage-dot stage-dot--2"><span>STAGE</span><b>2</b></div>

  <div class="abs stage-box stage-box--prior">
    <h2>PRIORITISE</h2>
    <p>From those we asked patients, carers, physiotherapists, nurses and surgeons to tell us</p>
    <p>“What are your top-10 most important questions”. This created a shortlist that were prioritized at a final workshop.</p>
  </div>
  <div class="abs stage-dot stage-dot--3"><span>STAGE</span><b>3</b></div>

  <div class="abs front-foot"></div>
</section>

<section class="page page--back" aria-label="Leaflet back">
  <svg class="abs heading-banner" viewBox="0 0 326 38" aria-hidden="true">
    <polygon points="0,19 18,0 308,0 326,19 308,38 18,38" fill="rgba(20,70,150,.7)"/>
  </svg>
  <div class="abs heading-banner"><h2>Our top-10 research priorities:</h2></div>

  <div class="abs priority priority--l" style="top:56px">What are the best ways to measure the outcome following lower limb orthopaedic surgery in children?</div>
  <div class="abs num num--l c-red" style="top:54px">1</div>

  <div class="abs priority priority--r" style="top:104px">Following orthopaedic surgery to the lower limbs, what should children’s rehabilitation include, how long is it expected to last and how does it affect the result of treatment?</div>
  <div class="abs num num--r c-green" style="top:102px">2</div>

  <div class="abs priority priority--l" style="top:152px">What is the short-term and long-term clinical and cost effectiveness of orthopaedic lower limb surgery (including best timing and technique) for children with Cerebral Palsy who can walk?</div>
  <div class="abs num num--l c-orange" style="top:150px">3</div>

  <div class="abs priority priority--r" style="top:200px">What are the short term and long term outcomes of surgery compared to non-surgical care in the treatment of Perthes disease of the hip?</div>
  <div class="abs num num--r c-purple" style="top:198px">4</div>

  <div class="abs priority priority--l" style="top:248px">What is the clinical and cost effectiveness of pre-operative rehabilitation in children presenting with lower limb orthopaedic conditions?</div>
  <div class="abs num num--l c-teal" style="top:246px">5</div>

  <div class="abs priority priority--r" style="top:296px">What is the short-term and long-term clinical and cost effectiveness of Selective Dorsal Rhizotomy (SDR) in children with Cerebral Palsy who can walk?</div>
  <div class="abs num num--r c-red" style="top:294px">6</div>

  <div class="abs priority priority--l" style="top:344px">Can surveillance and non-surgical treatment (e.g. physiotherapy, botulinum toxin injections, functional electrical stimulation, orthotics, casting) prevent the development of deformity requiring surgery in children with Cerebral Palsy?</div>
  <div class="abs num num--l c-green" style="top:342px">7</div>

  <div class="abs priority priority--r" style="top:392px">What is the best method of screening for Developmental Dysplasia of the Hip (DDH) in terms of clinical and cost effectiveness?</div>
  <div class="abs num num--r c-orange" style="top:390px">8</div>

  <div class="abs priority priority--l" style="top:440px">What are the best strategies to optimise communication of information between patients/carers and clinicians in order to enable shared decision-making?</div>
  <div class="abs num num--l c-purple" style="top:438px">9</div>

  <div class="abs priority priority--r" style="top:488px">What is the best management for hip displacement in children with Cerebral Palsy?</div>
  <div class="abs num num--r c-teal" style="top:486px">10</div>

  <div class="abs thanks-band">Many thanks to all those people who helped us take this work off the ground and helped us finish it!</div>

  <div class="abs sponsors">
    <div class="abs sponsors__label">Special<br>thanks to:</div>
    <div class="abs sponsor sponsor--guild"><i></i>Albion Orthopaedic Guild</div>
    <div class="abs sponsor sponsor--society"><i></i>NSPBS</div>
    <div class="abs sponsor sponsor--uni"><i></i>Kestrel University</div>
    <div class="abs sponsor-end">
      and the
      <div class="brand-name"><span class="brand-mark"></span>Harriet Voss Consortium</div>
      who always look for fair play in research!
    </div>
  </div>
  <div class="abs back-foot"></div>
</section>

</body>
</html>
```